Website for an AdOps/Media Agency

We need a logo for an ad operations firm. We help websites to maximize their advertising revenues by optimizing their ad networks, configurations, technologies, etc. The name is Zornival, or ZorNival, to communicate that we take them to the top of their revenue potential. We want to also communicate, trust us to handle your adops, we take care of the hassle (it's an industry in continual technological innovation -- hard to stay on top of, and heavily manual, reporting, etc) and make sure our clients maximize ad revenues. For more info on site ideas/desires: https://files.brelmora.com/doc/7QxTbn2Lw9Rk4Vz8Hc3Md6Fp1Ys5Ga0Je/view?usp=sharing
Updates

Project Deadline Extended Reason: Apologies, I got caught up in other things. This is now priority, and will be guaranteed. I will also include an extra coding fee for a WP site and increase the budget. Thanks for your understanding! Added Thursday, July 7, 2016

Target Market(s)

Ad Operations/Media Consultancy

Industry/Entity Type

Ad Agency

Number of Pages Required

1 page

Font styles to use
Sans Serif

Requirements
Must have
• I like clean and simple, nice images, scrolling down.
Nice to have
• I like clean, fresh white running through the site. Note, I listed us as an ad agency, but only because there was no adops. We work with ad agencies, but we are more agents for publishers.
Should not have
• To much clutter.

```html
<!DOCTYPE html>
<html lang="en">
<head>
<meta charset="utf-8">
<title>Zornival — AdOps</title>
<link href="https://fonts.googleapis.com/css2?family=Raleway:wght@300;400;500;600&family=Open+Sans:wght@400;600&display=swap" rel="stylesheet">
<style>
:root{
  --orange:#ff8a00;
  --orange-deep:#f07d00;
  --orange-btn:#e87900;
  --blue:#4a9be0;
  --ink:#3c3c3c;
  --muted:#8a8a8a;
  --line:#d6d6d6;
  --dark:#2b2f33;
  --darker:#23272a;
  --white:#ffffff;
}
*{box-sizing:border-box;margin:0;padding:0}
html,body{width:1200px;height:2258px;overflow:hidden;background:var(--white)}
body{position:relative;font-family:"Open Sans",Arial,sans-serif;color:var(--ink)}
.abs{position:absolute}

/* hero */
.hero{position:absolute;left:0;top:0;width:1200px;height:610px;
  background:linear-gradient(120deg,#ff9a1a 0%,var(--orange) 45%,#ff9f2a 70%,var(--orange-deep) 100%);overflow:hidden}
.hero-curve{position:absolute;left:0;top:540px;width:1200px;height:80px}
.logo{left:184px;top:30px;font-family:"Raleway",sans-serif;font-weight:400;font-size:38px;color:var(--white);letter-spacing:.5px}
.nav{left:491px;top:46px;display:flex;gap:0;font-family:"Raleway",sans-serif;font-size:15px;color:var(--white);font-weight:500}
.nav span{margin-right:36px}
.quote-btn{left:880px;top:38px;width:141px;height:37px;background:var(--orange-btn);color:var(--white);
  font-family:"Raleway",sans-serif;font-weight:500;font-size:14px;display:flex;align-items:center;justify-content:center}
.hero-title{left:0;top:140px;width:1200px;text-align:center;font-family:"Raleway",sans-serif;font-weight:600;
  font-size:36px;line-height:38px;color:var(--white);letter-spacing:.5px}
.read-more{left:539px;top:235px;width:127px;height:35px;border:2px solid var(--white);color:var(--white);
  font-family:"Raleway",sans-serif;font-size:12px;display:flex;align-items:center;justify-content:center;letter-spacing:.5px}
.arrow{top:266px;width:20px;height:34px}
.hero-art{left:226px;top:270px;width:760px;height:282px;border-radius:10px;
  background:radial-gradient(ellipse at 50% 45%,#7fc3f0 0%,#5aaee8 35%,rgba(255,180,90,.35) 75%,rgba(255,150,30,0) 100%)}

/* intro */
.intro-h1{left:0;top:624px;width:1200px;text-align:center;font-family:"Raleway",sans-serif;font-size:28px;color:var(--ink)}
.intro-h2{left:0;top:660px;width:1200px;text-align:center;font-family:"Raleway",sans-serif;font-size:23px;color:var(--ink)}
.intro-lead{left:230px;top:709px;width:740px;text-align:center;font-size:12px;line-height:18px;color:#444}
.intro-body{left:220px;top:757px;width:760px;text-align:center;font-size:12px;line-height:18px;color:var(--muted)}
.learn-orange{left:544px;top:833px;width:119px;height:36px;border-radius:18px;background:var(--orange);color:var(--white);
  font-family:"Raleway",sans-serif;font-weight:500;font-size:13px;display:flex;align-items:center;justify-content:center}

/* partnership */
.partner{left:0;top:920px;width:600px;height:384px;background:var(--blue)}
.partner-photo{left:600px;top:920px;width:600px;height:384px;
  background:linear-gradient(135deg,#5b4636 0%,#e9e6df 30%,#f1efe9 55%,#c7b9a4 80%,#4d3b2e 100%)}
.partner-title{left:187px;top:982px;font-family:"Raleway",sans-serif;font-size:27px;color:var(--white)}
.partner-text{left:187px;top:1028px;width:372px;font-size:11.5px;line-height:17.5px;color:var(--white)}
.partner-text p+p{margin-top:10px}
.learn-outline{left:190px;top:1197px;width:119px;height:35px;border:2px solid var(--white);border-radius:18px;color:var(--white);
  font-family:"Raleway",sans-serif;font-size:13px;display:flex;align-items:center;justify-content:center}

/* services */
.services-title{left:0;top:1346px;width:1200px;text-align:center;font-family:"Raleway",sans-serif;font-size:26px;color:#555}
.service{width:440px;height:80px}
.service-icon{position:absolute;left:0;top:0;width:78px;height:78px;border:2px solid var(--line);border-radius:50%;
  display:flex;align-items:center;justify-content:center;background:var(--white)}
.service-name{position:absolute;left:94px;top:15px;width:330px;font-family:"Raleway",sans-serif;font-weight:500;font-size:16.5px;line-height:18px;color:#222}
.service-desc{position:absolute;left:94px;top:38px;width:320px;font-size:10.5px;line-height:16px;color:#666}
.service-desc.low{top:56px}

/* contact */
.contact{left:0;top:1822px;width:1200px;height:377px;
  background:radial-gradient(ellipse at 80% 20%,#3a3f44 0%,var(--dark) 55%,#1f2326 100%)}
.contact-title{left:0;top:1872px;width:1200px;text-align:center;font-family:"Raleway",sans-serif;font-size:26px;color:var(--white)}
.field{left:253px;width:369px;border:1px solid #8c9094;background:rgba(20,22,25,.35);color:var(--white);
  font-size:10.5px;padding:9px 14px;letter-spacing:.3px}
.submit{left:253px;top:2095px;width:90px;height:33px;background:var(--blue);color:var(--white);font-size:12px;font-weight:600;
  display:flex;align-items:center;justify-content:center;letter-spacing:.5px}
.info{left:706px;color:var(--white);font-size:13.5px;line-height:19px;display:flex;gap:6px}
.social{left:703px;top:2050px;display:flex;gap:3px}
.social span{width:28px;height:28px;border:1.5px solid var(--white);border-radius:50%}

/* footer */
.footer{left:0;top:2199px;width:1200px;height:59px;background:var(--darker)}
.footer-text{left:181px;top:2216px;font-size:11px;color:#bfc2c4}
</style>
</head>
<body>

<header class="hero">
  <svg class="hero-curve" viewBox="0 0 1200 80" preserveAspectRatio="none" aria-hidden="true">
    <path d="M0 62 C300 20 800 -5 1200 28 L1200 80 L0 80 Z" fill="#ffffff"/>
  </svg>
</header>
<div class="abs logo">Zornival</div>
<nav class="abs nav"><span>About Us</span><span>Services</span><span>Clients</span><span>Resources</span></nav>
<div class="abs quote-btn">Request a Quote</div>
<h1 class="abs hero-title">ONESTOP SHOP FOR ALL YOUR<br>ADOPS NEEDS</h1>
<div class="abs read-more">READ MORE</div>
<svg class="abs arrow" style="left:132px" viewBox="0 0 20 34" aria-hidden="true"><path d="M16 3 L4 17 L16 31" fill="none" stroke="#fff" stroke-width="3.5"/></svg>
<svg class="abs arrow" style="left:1046px" viewBox="0 0 20 34" aria-hidden="true"><path d="M4 3 L16 17 L4 31" fill="none" stroke="#fff" stroke-width="3.5"/></svg>
<div class="abs hero-art" role="img" aria-label="Flat illustration of a laptop with a megaphone surrounded by a clock, globe, shopping basket, envelope and chat bubbles"></div>

<section>
  <h2 class="abs intro-h1">Let our team help YOUR team Optimize your</h2>
  <h3 class="abs intro-h2">adops and maximize your monetization</h3>
  <p class="abs intro-lead">We can help you take your revenues to the next level. Our team will work handinhand with yourteam to ensure that things run smoothly, optimally, and for the best possible returns. graphics: climbers climbing up a hill?</p>
  <p class="abs intro-body">Curabitur vel mi sit amet magna malesuada ultrices Ut nisi erat fermentum vel congue id euismod in elit Fusce ultricies orci ac feugiat suscipit leo massa sodales velit et scelerisque mi tortor at ipsum cligula augue bibendum accumsan vestibulum ut commodo a mi Morbi ornare gravida elit Integer congue augue et malesuada iaculis ipsum dui aliquet felis</p>
  <div class="abs learn-orange">Learn More</div>
</section>

<section>
  <div class="abs partner"></div>
  <div class="abs partner-photo" role="img" aria-label="Photo of a table covered in colour swatches and printed charts with the word Advertising"></div>
  <h2 class="abs partner-title">Publisher Partnership</h2>
  <div class="abs partner-text">
    <p>Programmatic has revolutionized the advertising playing field. Now, small, medium and large publishers alike all have equal access to the best advertisers and premium cpms. But it's a fast moving world, and it takes a big team and varied skill set to stay on top of the technologies, players, offers, implementations and optimizations.</p>
    <p>Our team covers all these skills, and our team wants to be on your team. We work with top publishers helping to maximize their monetization on over 1.5B monthly impressions.</p>
  </div>
  <div class="abs learn-outline">Learn More</div>
</section>

<section>
  <h2 class="abs services-title">Services Provides</h2>

  <div class="abs service" style="left:179px;top:1414px">
    <div class="service-icon"><svg width="40" height="40" viewBox="0 0 40 40" aria-hidden="true"><g fill="#ff8a00"><rect x="6" y="33" width="16" height="4"/><path d="M9 32 L11 22 H17 L19 32 Z"/><circle cx="14" cy="18" r="4"/><rect x="23" y="33" width="13" height="4"/><path d="M25 32 L27 15 H32 L34 32 Z"/><rect x="26" y="9" width="7" height="5"/><rect x="28.5" y="3" width="2" height="6"/><rect x="26.5" y="5" width="6" height="2"/></g></svg></div>
    <div class="service-name">Monetization Strategy &amp; Planning</div>
    <div class="service-desc">There's no "one size fits all" ads strategy. We help you find the winning combination, placements and mix for your adspace offer</div>
  </div>

  <div class="abs service" style="left:630px;top:1414px">
    <div class="service-icon"><svg width="40" height="40" viewBox="0 0 40 40" aria-hidden="true"><g fill="#ff8a00"><rect x="2" y="12" width="7" height="15"/><rect x="31" y="12" width="7" height="15"/><path d="M10 14 L18 12 L24 15 L30 14 V25 L22 30 L10 25 Z"/></g><path d="M16 17 L21 20 M19 22 L23 25" stroke="#fff" stroke-width="1.5"/></svg></div>
    <div class="service-name">Contract Negotiation</div>
    <div class="service-desc">There's no "one size fits all" ads strategy. We help you find the winning combination, placements and mix for your adspace offer</div>
  </div>

  <div class="abs service" style="left:179px;top:1532px">
    <div class="service-icon"><svg width="40" height="40" viewBox="0 0 40 40" aria-hidden="true"><circle cx="20" cy="20" r="15" fill="#ff8a00"/><path d="M11 13 C15 12 17 16 15 19 C13 22 17 24 16 28 M24 9 C23 13 28 14 27 18 C26 21 30 23 32 22" fill="none" stroke="#fff" stroke-width="2.2"/></svg></div>
    <div class="service-name">Network Configurations</div>
    <div class="service-desc">From header bidders, to video, to native, to display, we create your optimum mix for maximum monetization: Screening, implementation</div>
  </div>

  <div class="abs service" style="left:630px;top:1532px">
    <div class="service-icon"><svg width="40" height="40" viewBox="0 0 40 40" aria-hidden="true"><g fill="#ff8a00"><circle cx="20" cy="7" r="4"/><rect x="15" y="12" width="10" height="6"/><rect x="19" y="18" width="2" height="4"/><rect x="7" y="21" width="26" height="2"/><rect x="7" y="22" width="2" height="4"/><rect x="19" y="22" width="2" height="4"/><rect x="31" y="22" width="2" height="4"/><circle cx="8" cy="29" r="3"/><circle cx="20" cy="29" r="3"/><circle cx="32" cy="29" r="3"/><rect x="4" y="33" width="8" height="4"/><rect x="16" y="33" width="8" height="4"/><rect x="28" y="33" width="8" height="4"/></g></svg></div>
    <div class="service-name">Relationship Management</div>
    <div class="service-desc">We help to make sure you are getting the best possible pricing and terms, and keep the relations to make sure the premium offers keep coming your way.</div>
  </div>

  <div class="abs service" style="left:179px;top:1654px">
    <div class="service-icon"><svg width="40" height="40" viewBox="0 0 40 40" aria-hidden="true"><rect x="7" y="10" width="22" height="22" rx="3" fill="none" stroke="#ff8a00" stroke-width="3"/><path d="M16 25 L18 19 L31 6 L35 10 L22 23 Z" fill="#ff8a00"/></svg></div>
    <div class="service-name">Access to our Premium Ad Exchange Account</div>
    <div class="service-desc low">From header bidders, to video, to native, to display, we create your optimum mix for maximum monetization: Screening.</div>
  </div>

  <div class="abs service" style="left:630px;top:1654px">
    <div class="service-icon"><svg width="40" height="40" viewBox="0 0 40 40" aria-hidden="true"><g fill="#ff8a00"><rect x="6" y="6" width="2.5" height="28"/><rect x="6" y="31.5" width="29" height="2.5"/><rect x="12" y="20" width="4" height="10"/><rect x="18" y="14" width="4" height="16"/><rect x="24" y="18" width="4" height="12"/><rect x="30" y="10" width="4" height="20"/></g></svg></div>
    <div class="service-name">Campaign Performance &amp; Reporting</div>
    <div class="service-desc">Daily reporting, continuous monitoring for performance and discrepancies</div>
  </div>
</section>

<section>
  <div class="abs contact" role="img" aria-label="Dark photo of hands working at a desk with a keyboard"></div>
  <h2 class="abs contact-title">CONTACT US</h2>
  <div class="abs field" style="top:1938px;height:32px">YOUR NAME</div>
  <div class="abs field" style="top:1977px;height:32px">EMAIL ADDRESS</div>
  <div class="abs field" style="top:2016px;height:71px">MESSAGE</div>
  <div class="abs submit">SUBMIT</div>

  <div class="abs info" style="top:1933px">
    <svg width="12" height="18" viewBox="0 0 12 18" aria-hidden="true" style="margin-top:1px"><path d="M6 0 C2.7 0 0 2.6 0 5.9 C0 10 6 18 6 18 C6 18 12 10 12 5.9 C12 2.6 9.3 0 6 0 Z" fill="#fff"/><circle cx="6" cy="6" r="2.3" fill="#2b2f33"/></svg>
    <span>412 Marlow Park Road Suite B20<br>Fenwick, PA 19388</span>
  </div>
  <div class="abs info" style="top:1991px">
    <svg width="14" height="16" viewBox="0 0 14 16" aria-hidden="true" style="margin-top:2px"><path d="M3 0 L6 4 L4.5 6 C5.5 8.5 7 10 9 11 L11 9.5 L14 12.5 L12 15.5 C6 15 1 10 0 3 Z" fill="#fff"/></svg>
    <span>06 31 58 42</span>
  </div>
  <div class="abs info" style="top:2019px">
    <svg width="15" height="12" viewBox="0 0 15 12" aria-hidden="true" style="margin-top:4px"><rect width="15" height="12" fill="#fff"/><path d="M0 0 L7.5 6.5 L15 0" fill="none" stroke="#2b2f33" stroke-width="1.3"/></svg>
    <span>hello@zornival-studio.com</span>
  </div>
  <div class="abs social"><span></span><span></span><span></span><span></span></div>
</section>

<footer>
  <div class="abs footer"></div>
  <div class="abs footer-text">© 2016 Company Name&nbsp; All right reserved&nbsp; Term of Use</div>
</footer>

</body>
</html>
```